strength and conditioning business focused on helping people move more efficiently

I need a business card designed for a Philadelphia based company called Trk Vlt Motion (pronounced Track Volt). We offer fitness professional services with the idea of helping people feel better and move optimally. We do this by designing and walking through individualized programs as well as minor soft tissue work. Our perfect client would be athletes but we will be marketing to parents who have children that are active They remember their former athletic days and want to get as close as possible back to that feeling. Attached will be the official logo and logo formats. I would love for the design to communicate trustworthy and creative. I would also love for the design to be square with rounded edges.

Target Market(s)

Parents of athletic children
former athletes
athletes

Industry/Entity Type

Fitness

Contact Information for Business Card

Business: Trk Vlt Performance
Name: Coach Garrett Ellison
Position: Strength and Conditioning Coach / Certified Personal Trainer
Contact: coach.ell@trkvlt-example.com
Text: (555)204-7719

Font styles to use
Serif
Sans Serif

Colors
fbee38
fbee3e
0255a3
3176b5
ffffff

Requirements
Must have
• use of logo
Nice to have
• Square design
rounded edges

```html
<!DOCTYPE html>
<html lang="en">
<head>
<meta charset="utf-8">
<title>Trk Vlt Motion – Business Card</title>
<link rel="stylesheet" href="https://fonts.googleapis.com/css2?family=Open+Sans:wght@400;800&family=Montserrat:wght@700&display=swap">
<style>
  :root {
    --navy: #0a2a6e;
    --yellow: #f2c21a;
    --paper: #ffffff;
    --ink: #333333;
    --backdrop: #dcdcdc;
  }
  * { margin: 0; padding: 0; box-sizing: border-box; }
  html, body { width: 1200px; height: 908px; overflow: hidden; }
  body {
    background: var(--backdrop);
    font-family: "Open Sans", Arial, sans-serif;
    position: relative;
  }
  .card {
    position: absolute;
    top: 224px;
    width: 460px;
    height: 460px;
    border-radius: 48px;
    overflow: hidden;
  }
  .card--front { left: 80px; background: var(--navy); display: flex; align-items: center; justify-content: center; }
  .card--back { left: 660px; background: var(--paper); padding: 78px 34px 0 34px; }

  .brand { display: flex; align-items: center; gap: 14px; }
  .brand__dot { width: 42px; height: 42px; border-radius: 50%; background: var(--yellow); flex: none; }
  .brand__name { font-weight: 800; font-size: 40px; letter-spacing: -0.5px; line-height: 1; white-space: nowrap; }
  .card--front .brand__name { color: var(--paper); }
  .card--back .brand__name { color: var(--navy); }

  .coach-name {
    margin-top: 70px;
    font-family: "Montserrat", Arial, sans-serif;
    font-weight: 700;
    font-size: 18px;
    letter-spacing: 3px;
    color: var(--navy);
    white-space: nowrap;
  }
  .rule { height: 1.5px; background: var(--yellow); margin: 10px 0; }
  .role { font-size: 11.5px; color: var(--ink); white-space: nowrap; }
  .contact { display: flex; justify-content: space-between; font-size: 9.5px; color: var(--ink); white-space: nowrap; }
  .contact__item { display: flex; align-items: center; gap: 3px; }
  .contact__item svg { width: 10px; height: 10px; fill: var(--navy); flex: none; }
</style>
</head>
<body>
  <section class="card card--front">
    <div class="brand">
      <span class="brand__dot"></span>
      <span class="brand__name">Trk Vlt Motion</span>
    </div>
  </section>

  <section class="card card--back">
    <div class="brand">
      <span class="brand__dot"></span>
      <span class="brand__name">Trk Vlt Motion</span>
    </div>
    <h1 class="coach-name">COACH GARRETT ELLISON</h1>
    <div class="rule"></div>
    <p class="role">Strength and Conditioning Coach / Certified Personal Trainer</p>
    <div class="rule"></div>
    <div class="contact">
      <span class="contact__item">
        <svg viewBox="0 0 12 12"><circle cx="6" cy="6" r="6"/><path d="M4 3.5l1 1-.6.8c.4.8 1 1.4 1.8 1.8l.8-.6 1 1-.7.9C5.4 8.2 3.8 6.6 3.6 4.2z" fill="#fff"/></svg>
        (555)204-7719
      </span>
      <span class="contact__item">
        <svg viewBox="0 0 12 12"><rect x="0.5" y="2" width="11" height="8" rx="1"/><path d="M1 2.5l5 4 5-4" stroke="#fff" fill="none"/></svg>
        coach.ell@trkvlt-example.com
      </span>
      <span class="contact__item">
        <svg viewBox="0 0 12 12"><circle cx="6" cy="6" r="6"/><path d="M0 6h12M6 0c-3 3-3 9 0 12M6 0c3 3 3 9 0 12" stroke="#fff" fill="none" stroke-width=".8"/></svg>
        www.trkvlt-example.com
      </span>
    </div>
  </section>
</body>
</html>
```